Bindle Crest Mustard - Australian Iconic Label

Label design. This first label will be part of a growing set of Australian Condiments. We would like the label to be iconic of Australia. We would like to sell this product as an Australian souvenir at airports, Australiana gift stores, tourism destinations etc. We would like an Australian iconic image to sit in the background on the centre diamond. We would prefer it was not limited to regional icons more generic icons for example kangaroo and emu so it doesn't matter which state or destination it is sold. This range can look different to our other range of products as they will not necessarily sell at the same places but we would still like customers to identify that they are Pellham's Bites. I've included some other labels we use on this jar so you can replicate colours and size of the label (details on files + width of band 35mm).
P.s. it requires a sealing tab integrated into the design.
Brand name: Pellham's Bites
Produced at The Morsel Works
www.morselworks.com.au
IF you would like any further direction please don't hesitate to ask.

Target Market(s)

Tourism
Souvenir
Gift

```html
<!DOCTYPE html>
<html lang="en">
<head>
<meta charset="utf-8">
<title>Bindle Crest Mustard – Label</title>
<link rel="stylesheet" href="https://fonts.googleapis.com/css2?family=Marcellus&family=Montserrat:wght@700&family=Roboto+Condensed:wght@500&display=swap">
<style>
  :root {
    --backdrop-light: #c9ab2c;
    --backdrop-dark: #8a7019;
    --label-green: #0f8a3f;
    --label-yellow: #fcd21c;
    --floral-yellow: #f7d93a;
    --floral-pale: #fbeea0;
    --panel-white: #f4f4f2;
    --ink: #1a1a1a;
    --white: #ffffff;
  }
  html, body {
    margin: 0;
    padding: 0;
    overflow: hidden;
  }
  .canvas {
    position: relative;
    width: 1200px;
    height: 1200px;
    overflow: hidden;
    background: radial-gradient(ellipse at 50% 85%, var(--backdrop-light), var(--backdrop-dark) 75%);
  }
  .label-art {
    position: absolute;
    inset: 0;
  }
  .diamond-copy {
    position: absolute;
    left: 300px;
    width: 600px;
    top: 528px;
    text-align: center;
  }
  .brand-name {
    font-family: "Montserrat", sans-serif;
    font-weight: 700;
    font-size: 21px;
    line-height: 30px;
    letter-spacing: 0.32em;
    color: var(--label-green);
    margin: 0 0 4px 0.32em;
  }
  .product-name {
    font-family: "Marcellus", serif;
    color: var(--ink);
    margin: 0;
    font-weight: 400;
  }
  .product-name .product-main {
    display: block;
    font-size: 92px;
    line-height: 88px;
    letter-spacing: 0.02em;
  }
  .product-name .product-sub {
    display: block;
    font-size: 38px;
    line-height: 46px;
    letter-spacing: 0.01em;
  }
  .origin-pill {
    display: inline-block;
    margin-top: 28px;
    padding: 5px 22px 6px;
    border-radius: 20px;
    background: var(--label-green);
    color: var(--white);
    font-family: "Roboto Condensed", sans-serif;
    font-weight: 500;
    font-size: 19px;
    box-shadow: 0 0 0 2px var(--white), 0 0 0 4px var(--label-green);
  }
</style>
</head>
<body>
<main class="canvas">
  <svg class="label-art" width="1200" height="1200" viewBox="0 0 1200 1200" xmlns="http://www.w3.org/2000/svg">
    <defs>
      <pattern id="star-row" x="0" y="0" width="34" height="44" patternUnits="userSpaceOnUse">
        <polygon points="17,12 19.6,19 27,19 21,23.5 23.3,31 17,26.5 10.7,31 13,23.5 7,19 14.4,19" fill="var(--label-green)"/>
      </pattern>
      <linearGradient id="floral-tone" x1="0" y1="0" x2="0" y2="1">
        <stop offset="0" stop-color="var(--floral-pale)"/>
        <stop offset="0.5" stop-color="var(--floral-yellow)"/>
        <stop offset="1" stop-color="var(--floral-pale)"/>
      </linearGradient>
    </defs>

    <!-- sealing tab -->
    <g class="seal-tab">
      <rect x="570" y="40" width="60" height="320" fill="var(--label-yellow)"/>
      <rect x="582" y="40" width="36" height="320" fill="var(--label-green)"/>
    </g>

    <!-- wrap band -->
    <g class="wrap-band">
      <rect x="60" y="470" width="1080" height="330" fill="var(--label-yellow)"/>
      <rect x="60" y="470" width="1080" height="44" fill="url(#star-row)"/>
      <rect x="60" y="515" width="1080" height="7" fill="var(--label-green)"/>
      <rect x="60" y="526" width="1080" height="220" fill="url(#floral-tone)" role="img" aria-label="Pattern of yellow wattle and mustard blossoms with green leaves"/>
      <rect x="60" y="750" width="1080" height="7" fill="var(--label-green)"/>
      <rect x="60" y="757" width="1080" height="44" fill="url(#star-row)"/>
    </g>

    <!-- centre diamond -->
    <g class="centre-diamond">
      <polygon points="600,320 930,635 600,950 270,635" fill="var(--label-yellow)"/>
      <polygon points="600,328 921,635 600,942 279,635" fill="var(--label-green)"/>
      <polygon points="600,346 903,635 600,924 297,635" fill="var(--label-yellow)"/>
      <polygon points="600,352 897,635 600,918 303,635" fill="var(--label-green)"/>
      <polygon points="600,360 889,635 600,910 311,635" fill="var(--panel-white)" role="img" aria-label="Faint Australian icon artwork of kangaroo and emu among blossoms"/>
    </g>
  </svg>

  <div class="diamond-copy">
    <p class="brand-name">PELLHAM'S<br>BITES</p>
    <h1 class="product-name">
      <span class="product-main">BINDLE</span>
      <span class="product-sub">CREST MUSTARD</span>
    </h1>
    <span class="origin-pill">Proudly Australian Owned &amp; Made</span>
  </div>
</main>
</body>
</html>
```